Morden, Creative, Unique, Independent Wine Shop

1. We are a brand new wine shop located in Melbourne Australia, we have our logo already, simply use the logo to design a business card.
2. I have uploaded our logo in two versions, with or without shadow, any of them is acceptable.
3. Make it as creative and unique as possible, no limitation of shape, color combination, geometry pattern, fonts, composing etc.
3. Info on the card:
- Brambleford Wine Cellar (Not very necessary if logo is obviously shown)
- 42 Ferncastle Steet, Hampton, Victoria, Australia 3188
- +61 3 9018 4637
- www.bramblefordwinecellar.com.au
- bramblefordwinecellar@mailvista.com
- Additional icons: Google, Instagram, Facebook, Twitter
4. Once again, forget it is a commercial card, make it special.

```html
<!DOCTYPE html>
<html lang="en">
<head>
<meta charset="utf-8">
<title>Brambleford Wine Cellar — Business Card</title>
<link rel="stylesheet" href="https://fonts.googleapis.com/css2?family=Lato:wght@400;700&display=swap">
<style>
  :root {
    --bg: #d9d9d9;
    --card: #f4f4f4;
    --wine: #a3163f;
    --ink: #3c3c3c;
    --muted: #6b6b6b;
    --rule: #8a8a8a;
  }
  * { box-sizing: border-box; margin: 0; padding: 0; }
  html, body { width: 1200px; height: 1021px; overflow: hidden; }
  body {
    background: var(--bg);
    font-family: "Lato", sans-serif;
    color: var(--ink);
    position: relative;
  }
  .card {
    position: absolute;
    left: 197px;
    width: 806px;
    height: 460px;
    background: var(--card);
    box-shadow: 0 6px 18px rgba(0,0,0,.18);
  }
  .card--front { top: 35px; }
  .card--back { top: 526px; }

  .brand {
    display: flex;
    align-items: center;
    gap: 14px;
    color: var(--wine);
    font-weight: 400;
    letter-spacing: .04em;
  }
  .brand__dot {
    border-radius: 50%;
    background: var(--wine);
    flex: none;
  }

  .card--front .brand {
    position: absolute;
    left: 0; right: 0; top: 0; bottom: 0;
    justify-content: center;
    font-size: 40px;
    gap: 24px;
  }
  .card--front .brand__dot { width: 120px; height: 120px; }

  .card--back .brand {
    position: absolute;
    left: 48px; top: 48px;
    font-size: 24px;
  }
  .card--back .brand__dot { width: 46px; height: 46px; }

  .person { position: absolute; left: 250px; top: 160px; }
  .person__name { color: var(--wine); font-weight: 700; font-size: 26px; }
  .person__role { color: var(--muted); font-size: 18px; margin-top: 2px; }

  .divider {
    position: absolute;
    left: 250px;
    width: 40px;
    height: 2px;
    background: var(--rule);
  }
  .divider--a { top: 240px; }
  .divider--b { top: 396px; }

  .contact {
    position: absolute;
    left: 310px; top: 222px;
    font-size: 18px;
    line-height: 26px;
    color: var(--ink);
    list-style: none;
  }
  .contact li { display: flex; align-items: center; gap: 8px; }
  .contact__icon { width: 14px; height: 14px; flex: none; }
  .contact__web span { color: var(--wine); }

  .social {
    position: absolute;
    left: 310px; top: 386px;
    display: flex;
    gap: 22px;
    list-style: none;
  }
  .social li {
    width: 20px; height: 20px;
    border-radius: 50%;
    background: var(--wine);
  }
</style>
</head>
<body>

<section class="card card--front">
  <div class="brand">
    <span class="brand__dot"></span>
    <span class="brand__name">Brambleford Wine Cellar</span>
  </div>
</section>

<section class="card card--back">
  <div class="brand">
    <span class="brand__dot"></span>
    <span class="brand__name">Brambleford Wine Cellar</span>
  </div>

  <div class="person">
    <p class="person__name">Daniel Whitford</p>
    <p class="person__role">Founder</p>
  </div>

  <span class="divider divider--a"></span>

  <ul class="contact">
    <li>42 Ferncastle Steet, Hampton</li>
    <li>Victoria, Australia 3188</li>
    <li>
      <svg class="contact__icon" viewBox="0 0 16 16"><path fill="#a3163f" d="M3.5 1.5l2.5 3-1.5 1.5c.8 2 2.5 3.7 4.5 4.5l1.5-1.5 3 2.5-1.5 2.5C6.5 14 2 9.5 1 3z"/></svg>
      +61 3 9018 4637
    </li>
    <li>
      <svg class="contact__icon" viewBox="0 0 16 16"><rect x="1.5" y="3.5" width="13" height="9" fill="none" stroke="#a3163f" stroke-width="1.5"/><path d="M1.5 3.5l6.5 5 6.5-5" fill="none" stroke="#a3163f" stroke-width="1.5"/></svg>
      bramblefordwinecellar@mailvista.com
    </li>
    <li class="contact__web">
      <svg class="contact__icon" viewBox="0 0 16 16"><circle cx="8" cy="8" r="6.5" fill="none" stroke="#a3163f" stroke-width="1.4"/><ellipse cx="8" cy="8" rx="2.8" ry="6.5" fill="none" stroke="#a3163f" stroke-width="1.2"/><path d="M1.5 8h13" stroke="#a3163f" stroke-width="1.2"/></svg>
      www.<span>bramblefordwinecellar</span>.com.au
    </li>
  </ul>

  <span class="divider divider--b"></span>

  <ul class="social" aria-label="Social profiles">
    <li></li><li></li><li></li><li></li>
  </ul>
</section>

</body>
</html>
```